Simplified Double Diamond Diagram for Book

I need a simplified version of the Double Diamond Diagram for a book I am working on. I would like to represent the diagram with the following image/text:
- Two diamonds connected (as in each of the sample photos)
- Inclusion of "Diverge" "Converge" above each of the sides of the diamonds as shown in sample image 1 - without elaborative text
- Inclusion of "Problem" and "Solution" in each diamond as is shown in the example image 2
- I need a color version and black/white version of the image that can be turned into a mono-color version in the book.

```html
<!DOCTYPE html>
<html lang="en">
<head>
<meta charset="utf-8">
<title>Double Diamond Diagram</title>
<link rel="stylesheet" href="https://fonts.googleapis.com/css2?family=Poppins:wght@600;700&display=swap">
<style>
  :root {
    --paper: #ffffff;
    --ink: #000000;
    --green-start: #1a9e80;
    --green-end: #9bbb58;
    --green-edge: #21907a;
    --amber-start: #f0a020;
    --amber-end: #c0392b;
    --amber-edge: #e85a10;
    --blue-deep: #1976d2;
    --blue-light: #62a6ec;
    --navy: #0d2a4a;
    --orange-deep: #f5973f;
    --orange-light: #f2b985;
    --orange-edge: #e35a0c;
    --orange-pill: #e0540c;
    --mono-label: #666666;
    --mono-dash: #777777;
  }
  html, body { margin: 0; padding: 0; overflow: hidden; background: var(--paper); }
  .canvas { width: 1200px; height: 1200px; display: block; }
  .phase-label { font-family: "Poppins", sans-serif; font-weight: 700; font-size: 17px; fill: var(--ink); text-anchor: middle; dominant-baseline: middle; letter-spacing: 0.3px; }
  .pill-label { font-family: "Poppins", sans-serif; font-weight: 700; font-size: 17px; fill: #ffffff; text-anchor: middle; dominant-baseline: central; }
  .stage-name { font-family: "Poppins", sans-serif; font-weight: 600; font-size: 19px; fill: #ffffff; text-anchor: middle; dominant-baseline: central; }
  .stage-name--mono { fill: var(--mono-label); }
  .node { fill: var(--ink); }
  .diamond--green { fill: url(#grad-green); stroke: var(--green-edge); stroke-width: 2.5; }
  .diamond--amber { fill: url(#grad-amber); stroke: var(--amber-edge); stroke-width: 2.5; }
  .half--blue-deep { fill: var(--blue-deep); }
  .half--blue-light { fill: var(--blue-light); }
  .half--orange-deep { fill: var(--orange-deep); }
  .half--orange-light { fill: var(--orange-light); }
  .edge--navy { fill: none; stroke: var(--navy); stroke-width: 2.5; }
  .edge--orange { fill: none; stroke: var(--orange-edge); stroke-width: 2.5; }
  .pill--navy { fill: var(--navy); }
  .pill--orange { fill: var(--orange-pill); }
  .diamond--mono { fill: none; stroke: var(--ink); stroke-width: 2.5; }
  .axis--mono { stroke: var(--mono-dash); stroke-width: 2; stroke-dasharray: 7 6; }
</style>
</head>
<body>
<svg class="canvas" viewBox="0 0 1500 1500" xmlns="http://www.w3.org/2000/svg">
  <defs>
    <linearGradient id="grad-green" x1="0" y1="0" x2="1" y2="0">
      <stop offset="0" stop-color="var(--green-start)"/>
      <stop offset="1" stop-color="var(--green-end)"/>
    </linearGradient>
    <linearGradient id="grad-amber" x1="0" y1="0" x2="1" y2="0">
      <stop offset="0" stop-color="var(--amber-start)"/>
      <stop offset="1" stop-color="var(--amber-end)"/>
    </linearGradient>
  </defs>

  <!-- Gradient version, unlabelled -->
  <g class="set set--gradient">
    <polygon class="diamond--green" points="48,280 208,120 370,280 208,440"/>
    <polygon class="diamond--amber" points="372,280 534,120 694,280 534,440"/>
    <circle class="node" cx="48" cy="280" r="6"/>
    <circle class="node" cx="371" cy="280" r="6"/>
    <circle class="node" cx="694" cy="280" r="6"/>
    <text class="phase-label" transform="translate(115 178) rotate(-45)">DIVERGE</text>
    <text class="phase-label" transform="translate(312 187) rotate(45)">CONVERGE</text>
    <text class="phase-label" transform="translate(441 178) rotate(-45)">DIVERGE</text>
    <text class="phase-label" transform="translate(638 187) rotate(45)">CONVERGE</text>
  </g>

  <!-- Gradient version, labelled -->
  <g class="set set--gradient-labelled">
    <polygon class="diamond--green" points="807,280 967,120 1129,280 967,440"/>
    <polygon class="diamond--amber" points="1131,280 1292,120 1452,280 1292,440"/>
    <circle class="node" cx="807" cy="280" r="6"/>
    <circle class="node" cx="1130" cy="280" r="6"/>
    <circle class="node" cx="1452" cy="280" r="6"/>
    <text class="phase-label" transform="translate(874 178) rotate(-45)">DIVERGE</text>
    <text class="phase-label" transform="translate(1071 187) rotate(45)">CONVERGE</text>
    <text class="phase-label" transform="translate(1199 178) rotate(-45)">DIVERGE</text>
    <text class="phase-label" transform="translate(1397 187) rotate(45)">CONVERGE</text>
    <text class="stage-name" x="965" y="280">PROBLEM</text>
    <text class="stage-name" x="1296" y="280">SOLUTION</text>
  </g>

  <!-- Two-tone version, unlabelled -->
  <g class="set set--twotone">
    <polygon class="half--blue-deep" points="48,755 209,595 209,915"/>
    <polygon class="half--blue-light" points="209,595 370,755 209,915"/>
    <polygon class="edge--navy" points="48,755 209,595 370,755 209,915"/>
    <polygon class="half--orange-deep" points="373,755 535,595 535,915"/>
    <polygon class="half--orange-light" points="535,595 696,755 535,915"/>
    <polygon class="edge--orange" points="373,755 535,595 696,755 535,915"/>
    <circle class="node" cx="48" cy="755" r="6"/>
    <circle class="node" cx="372" cy="755" r="6"/>
    <circle class="node" cx="696" cy="755" r="6"/>
    <g transform="translate(129 675) rotate(-45)"><rect class="pill--navy" x="-62" y="-16" width="124" height="32" rx="16"/><text class="pill-label">DIVERGE</text></g>
    <g transform="translate(288 675) rotate(45)"><rect class="pill--navy" x="-70" y="-16" width="140" height="32" rx="16"/><text class="pill-label">CONVERGE</text></g>
    <g transform="translate(455 675) rotate(-45)"><rect class="pill--orange" x="-62" y="-16" width="124" height="32" rx="16"/><text class="pill-label">DIVERGE</text></g>
    <g transform="translate(614 675) rotate(45)"><rect class="pill--orange" x="-70" y="-16" width="140" height="32" rx="16"/><text class="pill-label">CONVERGE</text></g>
  </g>

  <!-- Two-tone version, labelled -->
  <g class="set set--twotone-labelled">
    <polygon class="half--blue-deep" points="804,755 966,595 966,915"/>
    <polygon class="half--blue-light" points="966,595 1127,755 966,915"/>
    <polygon class="edge--navy" points="804,755 966,595 1127,755 966,915"/>
    <polygon class="half--orange-deep" points="1130,755 1292,595 1292,915"/>
    <polygon class="half--orange-light" points="1292,595 1452,755 1292,915"/>
    <polygon class="edge--orange" points="1130,755 1292,595 1452,755 1292,915"/>
    <circle class="node" cx="804" cy="755" r="6"/>
    <circle class="node" cx="1129" cy="755" r="6"/>
    <circle class="node" cx="1452" cy="755" r="6"/>
    <g transform="translate(885 675) rotate(-45)"><rect class="pill--navy" x="-62" y="-16" width="124" height="32" rx="16"/><text class="pill-label">DIVERGE</text></g>
    <g transform="translate(1046 675) rotate(45)"><rect class="pill--navy" x="-70" y="-16" width="140" height="32" rx="16"/><text class="pill-label">CONVERGE</text></g>
    <g transform="translate(1211 675) rotate(-45)"><rect class="pill--orange" x="-62" y="-16" width="124" height="32" rx="16"/><text class="pill-label">DIVERGE</text></g>
    <g transform="translate(1372 675) rotate(45)"><rect class="pill--orange" x="-70" y="-16" width="140" height="32" rx="16"/><text class="pill-label">CONVERGE</text></g>
    <text class="stage-name" x="968" y="749">PROBLEM</text>
    <text class="stage-name" x="1288" y="749">SOLUTION</text>
  </g>

  <!-- Mono outline version, unlabelled -->
  <g class="set set--mono">
    <line class="axis--mono" x1="216" y1="1134" x2="216" y2="1446"/>
    <line class="axis--mono" x1="537" y1="1134" x2="537" y2="1446"/>
    <polygon class="diamond--mono" points="57,1290 216,1132 374,1290 216,1448"/>
    <polygon class="diamond--mono" points="378,1290 537,1132 695,1290 537,1448"/>
    <text class="phase-label" transform="translate(123 1182) rotate(-45)">DIVERGE</text>
    <text class="phase-label" transform="translate(318 1191) rotate(45)">CONVERGE</text>
    <text class="phase-label" transform="translate(445 1182) rotate(-45)">DIVERGE</text>
    <text class="phase-label" transform="translate(640 1191) rotate(45)">CONVERGE</text>
  </g>

  <!-- Mono outline version, labelled -->
  <g class="set set--mono-labelled">
    <line class="axis--mono" x1="963" y1="1134" x2="963" y2="1446"/>
    <line class="axis--mono" x1="1284" y1="1134" x2="1284" y2="1446"/>
    <polygon class="diamond--mono" points="805,1290 963,1132 1121,1290 963,1448"/>
    <polygon class="diamond--mono" points="1126,1290 1284,1132 1442,1290 1284,1448"/>
    <text class="phase-label" transform="translate(870 1182) rotate(-45)">DIVERGE</text>
    <text class="phase-label" transform="translate(1065 1191) rotate(45)">CONVERGE</text>
    <text class="phase-label" transform="translate(1192 1182) rotate(-45)">DIVERGE</text>
    <text class="phase-label" transform="translate(1387 1191) rotate(45)">CONVERGE</text>
    <text class="stage-name stage-name--mono" x="967" y="1284">PROBLEM</text>
    <text class="stage-name stage-name--mono" x="1282" y="1284">SOLUTION</text>
  </g>
</svg>
</body>
</html>
```